Bramwell Business Cards

Logo files are included. Full "Bramwell" logo should be included on the back of the business card. The B symbol should be included on the front with the contact information.

Bramwell, LLC is the company name and we do commercial construction and real estate development consulting services. Look for a fairly simple card design utilizing our logo.

```html
<!DOCTYPE html>
<html lang="en">
<head>
<meta charset="utf-8">
<title>Bramwell Business Cards</title>
<link rel="stylesheet" href="https://fonts.googleapis.com/css2?family=Libre+Baskerville:wght@700&family=Inter:wght@400;500&family=Montserrat:wght@600&display=swap">
<style>
  :root {
    --navy: #13304a;
    --gold: #e7a715;
    --white: #ffffff;
    --paper: #f7f7f5;
    --stage: #e9eaec;
  }
  * { margin: 0; padding: 0; box-sizing: border-box; }
  html, body { width: 1200px; height: 874px; overflow: hidden; background: var(--stage); }
  .canvas { position: relative; width: 1200px; height: 874px; }
  .card {
    position: absolute; left: 320px; width: 560px; height: 320px;
    border-radius: 22px; overflow: hidden; background: var(--navy);
  }
  .card--back { top: 78px; }
  .card--front { top: 476px; }

  .brand-lockup {
    position: absolute; inset: 0;
    display: flex; align-items: center; justify-content: center; gap: 18px;
  }
  .brand-dot { width: 34px; height: 34px; border-radius: 50%; background: var(--gold); }
  .brand-name {
    font-family: "Montserrat", sans-serif; font-weight: 600;
    font-size: 52px; letter-spacing: 3px; color: var(--white);
  }

  .front-shape { position: absolute; inset: 0; }
  .contact { position: absolute; left: 30px; top: 52px; color: var(--white); }
  .contact__name {
    font-family: "Libre Baskerville", serif; font-weight: 700;
    font-size: 19px; letter-spacing: 0.5px;
  }
  .contact__title {
    font-family: "Inter", sans-serif; font-size: 13px; color: var(--gold); margin: 2px 0 12px;
  }
  .contact__list { list-style: none; font-family: "Inter", sans-serif; font-size: 13px; line-height: 17px; }
  .contact__list li { display: flex; align-items: flex-start; gap: 8px; }
  .contact__list svg { flex: none; width: 11px; height: 11px; margin-top: 3px; fill: var(--gold); }

  .front-brand {
    position: absolute; left: 330px; top: 0; width: 230px; height: 320px;
    display: flex; align-items: center; justify-content: center; gap: 10px;
  }
  .front-brand .brand-dot { width: 18px; height: 18px; }
  .front-brand .brand-name { font-size: 26px; letter-spacing: 1.5px; color: var(--navy); }
</style>
</head>
<body>
<main class="canvas">

  <section class="card card--back" aria-label="Card back">
    <div class="brand-lockup">
      <span class="brand-dot"></span>
      <span class="brand-name">BRAMWELL</span>
    </div>
  </section>

  <section class="card card--front" aria-label="Card front">
    <svg class="front-shape" viewBox="0 0 560 320" width="560" height="320">
      <path d="M372 0 C300 60 282 230 310 320 L560 320 L560 0 Z" fill="var(--paper)"/>
      <path d="M362 10 C300 80 284 220 300 320" fill="none" stroke="var(--gold)" stroke-width="4"/>
      <path d="M372 0 C350 16 338 30 328 46" fill="none" stroke="var(--navy)" stroke-width="5"/>
    </svg>

    <div class="contact">
      <h1 class="contact__name">DANIEL HARROW</h1>
      <p class="contact__title">President</p>
      <ul class="contact__list">
        <li><svg viewBox="0 0 12 12"><path d="M6 0a4 4 0 0 0-4 4c0 3 4 8 4 8s4-5 4-8a4 4 0 0 0-4-4zm0 5.5A1.5 1.5 0 1 1 6 2.5a1.5 1.5 0 0 1 0 3z"/></svg><span>4120 Larkspur Court<br>Cedar Bluff, Alaska 34590</span></li>
        <li><svg viewBox="0 0 12 12"><path d="M2.5 0.5l2 2.5-1.2 1.5a7 7 0 0 0 4.2 4.2L9 7.5l2.5 2-1.5 2C5 11.5 0.5 7 0.5 2z"/></svg><span>555-214-7730</span></li>
        <li><svg viewBox="0 0 12 12"><path d="M3 0h6v12H3zM4 1.5v8h4v-8z"/></svg><span>555-418-2296</span></li>
        <li><svg viewBox="0 0 12 12"><path d="M3 0h5v3H3zM1 4h10v7H1zM3 6v1h6V6z"/></svg><span>555-307-6142</span></li>
        <li><svg viewBox="0 0 12 12"><path d="M0 2h12v8H0zM1 3l5 3.5L11 3v-.2H1z" fill-rule="evenodd"/></svg><span>harrow@bramwell.com</span></li>
        <li><svg viewBox="0 0 12 12"><circle cx="6" cy="6" r="6"/></svg><span>www.bramwell.com</span></li>
      </ul>
    </div>

    <div class="front-brand">
      <span class="brand-dot"></span>
      <span class="brand-name">BRAMWELL</span>
    </div>
  </section>

</main>
</body>
</html>
```